Coffeeshop menu for filter tip

We want to have a cannabis (coffeeshop) menu in the size 25mm wide x 60mm wide. Some examples attached.

it must have the following text:
Menu

WEED p/g
Velotrine €16
Cinderfox €14
Tide Rambler €14
Marigolden €16
Grand Pelican €14
Copper Comet €14

HASH p/g
Baltic Ember €12
Harbor Velvet€11
Plum Rova €14
Dusk Maple €10

Target Market(s)

tourist in Amsterdam

Requirements
Nice to have
• cannabis sign leaf
• No Cigarettes allowed symbol

```html
<!DOCTYPE html>
<html lang="en">
<head>
<meta charset="utf-8">
<title>Coffeeshop Menu</title>
<link rel="stylesheet" href="https://fonts.googleapis.com/css2?family=Questrial&display=swap">
<style>
  :root {
    --bg: #141414;
    --panel: #050505;
    --yellow: #f4ef5c;
    --white: #f5f5f5;
    --grey: #9a9a9a;
    --leaf: rgba(120, 120, 60, 0.14);
  }
  * { margin: 0; padding: 0; box-sizing: border-box; }
  html, body { width: 1200px; height: 2880px; overflow: hidden; background: var(--bg); }
  .menu {
    position: relative; width: 1200px; height: 2880px; overflow: hidden;
    background: var(--bg);
    font-family: "Questrial", sans-serif;
  }
  .leaf-decor { position: absolute; border-radius: 50%; }
  .leaf-decor--top { left: 560px; top: -80px; width: 700px; height: 700px;
    background: radial-gradient(circle, var(--leaf), transparent 70%); }
  .leaf-decor--mid { left: 700px; top: 1000px; width: 700px; height: 800px;
    background: radial-gradient(circle, var(--leaf), transparent 70%); }
  .leaf-decor--low { left: 800px; top: 2000px; width: 600px; height: 600px;
    background: radial-gradient(circle, var(--leaf), transparent 70%); }

  .no-smoking {
    position: absolute; top: 40px; left: 216px;
    display: flex; align-items: center; gap: 30px;
    color: var(--white); font-size: 58px; letter-spacing: 0.32em; line-height: 1;
  }
  .no-smoking svg { width: 68px; height: 68px; }

  .section-title {
    position: absolute; display: flex; justify-content: space-between;
    color: var(--yellow); line-height: 1;
  }
  .section-title--weed { left: 224px; top: 160px; width: 712px; font-size: 140px; }
  .section-title--hash { left: 312px; top: 1520px; width: 680px; font-size: 135px; }

  .unit { position: absolute; color: var(--grey); font-size: 64px; line-height: 1; }
  .unit--weed { left: 1061px; top: 250px; }
  .unit--hash { left: 56px; top: 1598px; }

  .panel-weed { position: absolute; left: 163px; top: 312px; width: 1037px; height: 1128px; background: var(--panel); }
  .panel-hash { position: absolute; left: 0; top: 1520px; width: 1048px; height: 904px; }

  .price-list { position: absolute; list-style: none; }
  .price-list li { position: absolute; left: 0; right: 0; height: 176px; display: flex; align-items: center; }
  .item-name { color: var(--yellow); font-size: 100px; line-height: 1; white-space: nowrap; }
  .item-name.is-long { font-size: 90px; }
  .item-price { color: var(--white); font-size: 96px; line-height: 1; letter-spacing: -0.04em; }

  .price-list--weed { left: 213px; top: 368px; width: 960px; }
  .price-list--weed .item-price { margin-left: auto; }

  .price-list--hash { left: 30px; top: 1707px; width: 1010px; }
  .price-list--hash .item-price { width: 210px; }

  .skyline { position: absolute; left: 0; top: 2424px; width: 1200px; height: 232px;
    background: linear-gradient(180deg, #2a2a2a 0%, #101010 60%, #050505 100%); }
  .footer { position: absolute; left: 0; top: 2656px; width: 1200px; height: 224px; background: #000; }
  .footer-title {
    position: absolute; left: 248px; top: 2716px; width: 712px;
    display: flex; justify-content: space-between;
    color: var(--white); font-size: 135px; line-height: 1;
  }
</style>
</head>
<body>
<main class="menu">
  <div class="leaf-decor leaf-decor--top" role="img" aria-label="Faint cannabis leaf"></div>

  <div class="panel-weed"></div>
  <svg class="panel-hash" viewBox="0 0 1048 904" aria-hidden="true">
    <polygon points="0,8 144,8 264,136 1048,136 1048,904 0,904" fill="#050505"/>
  </svg>

  <div class="leaf-decor leaf-decor--mid" role="img" aria-label="Faint cannabis leaf"></div>
  <div class="leaf-decor leaf-decor--low" role="img" aria-label="Faint cannabis leaf"></div>

  <p class="no-smoking">NO CIGARETTES
    <svg viewBox="0 0 68 68" aria-label="No smoking">
      <circle cx="34" cy="34" r="30" fill="none" stroke="#f5f5f5" stroke-width="5"/>
      <rect x="14" y="30" width="34" height="9" fill="none" stroke="#f5f5f5" stroke-width="4"/>
      <line x1="52" y1="30" x2="52" y2="39" stroke="#f5f5f5" stroke-width="4"/>
      <line x1="13" y1="13" x2="55" y2="55" stroke="#f5f5f5" stroke-width="5"/>
    </svg>
  </p>

  <h1 class="section-title section-title--weed"><span>W</span><span>E</span><span>E</span><span>D</span></h1>
  <span class="unit unit--weed">p/g</span>

  <ul class="price-list price-list--weed">
    <li style="top:0"><span class="item-name">VELOTRINE</span><span class="item-price">€16</span></li>
    <li style="top:176px"><span class="item-name">CINDERFOX</span><span class="item-price">€14</span></li>
    <li style="top:352px"><span class="item-name is-long">TIDE RAMBLER</span><span class="item-price">€14</span></li>
    <li style="top:528px"><span class="item-name">MARIGOLDEN</span><span class="item-price">€16</span></li>
    <li style="top:704px"><span class="item-name is-long">GRAND PELICAN</span><span class="item-price">€14</span></li>
    <li style="top:880px"><span class="item-name is-long">COPPER COMET</span><span class="item-price">€14</span></li>
  </ul>

  <h2 class="section-title section-title--hash"><span>H</span><span>A</span><span>S</span><span>H</span></h2>
  <span class="unit unit--hash">p/g</span>

  <ul class="price-list price-list--hash">
    <li style="top:0"><span class="item-price">€12</span><span class="item-name">BALTIC EMBER</span></li>
    <li style="top:176px"><span class="item-price">€11</span><span class="item-name is-long">HARBOR VELVET</span></li>
    <li style="top:352px"><span class="item-price">€14</span><span class="item-name">PLUM ROVA</span></li>
    <li style="top:528px"><span class="item-price">€10</span><span class="item-name">DUSK MAPLE</span></li>
  </ul>

  <div class="skyline" role="img" aria-label="Amsterdam city skyline silhouette"></div>
  <div class="footer"></div>
  <h2 class="footer-title"><span>M</span><span>E</span><span>N</span><span>U</span></h2>
</main>
</body>
</html>
```